Business card design for Velvet Harbor

We need business cards designed for our new marketing consulting company, Velvet Harbor. Our services include marketing strategy, go-to-market and launch planning, growth strategy, and execution. We serve medical technology and health technology companies, from startups to well-established growth companies.

The business cards should feel professional, credible, reliable and trustworthy, and should instill confidence. Also bold, creative, and modern.

The design must use the Velvet Harbor logo.

The primary brand color is this orange: #FF5501
A secondary color that you can use is this gray: #282B2D
I would prefer only to use the orange and gray. But if you feel you really need an additional accent color (please use it very sparingly, as little as possible), you can use this blue for small accent purposes: #009FED

Attached are the logo files. The main logo is the one with a little bit of orange on the left and the rest is gray.

The business card should include the following:

Velvet Harbor logo
First name and last name
Title
Email address
Phone number and type (in whatever order looks best for the design
Website (the website does not need to be in the same block as the personal info)

For example:

Nessa Pryle
Founder & Principal
nessa@velvetharbor.com
+1.628.309.4156 mobile (can use "." or spaces in between blocks of numbers)
velvetharbor.com (somewhere on the card, it does not need to be with the personal info; and note that there is no "www." at the beginning)

Note that there will be no address listed on the business card.

Target Market(s)

Executives (CEO, head of marketing, head of sales) at medical technology and health technology companies, mostly in their 40s and older, well-educated, often with advanced degrees. They are strategic thinkers, responsible for budgets, and familiar with P&L. Their comfort with and trust in using outside consultants varies.

Industry/Entity Type

Medical technology and health technology companies.

Contact Information for Business Card

See project description

Font styles to use
Sans Serif

Requirements
Must have
• Logo and see Business card details section above.

```html
<!DOCTYPE html>
<html lang="en">
<head>
<meta charset="utf-8">
<title>Velvet Harbor — Business Card</title>
<link href="https://fonts.googleapis.com/css2?family=Roboto:wght@400;500&display=swap" rel="stylesheet">
<style>
  :root {
    --orange: #f35d22;
    --gray: #282b2d;
    --text: #2a2c2e;
    --line: #8a8c8e;
    --card-white: #f4f4f4;
    --backdrop: #1c1d1e;
    --white: #f2f2f2;
  }
  * { margin: 0; padding: 0; box-sizing: border-box; }
  html, body {
    width: 1200px;
    height: 899px;
    overflow: hidden;
    background: var(--backdrop);
    font-family: "Roboto", Arial, sans-serif;
  }
  .stage { position: relative; width: 1200px; height: 899px; }

  .card {
    position: absolute;
    left: 333px;
    width: 555px;
    height: 318px;
    overflow: hidden;
  }
  .card-front { top: 132px; background: var(--card-white); }
  .card-back  { top: 487px; background: var(--orange); }

  /* front */
  .front-brand {
    position: absolute;
    top: 36px;
    right: 36px;
    display: flex;
    align-items: center;
    gap: 8px;
  }
  .brand-dot {
    width: 22px; height: 22px;
    border-radius: 50%;
    background: var(--orange);
  }
  .brand-name {
    font-weight: 500;
    color: var(--gray);
    font-size: 14px;
    line-height: 15px;
    letter-spacing: 2px;
    text-transform: uppercase;
  }

  .person { position: absolute; left: 25px; top: 151px; }
  .person-name {
    font-size: 21px;
    font-weight: 500;
    color: var(--text);
    text-transform: uppercase;
    line-height: 24px;
  }
  .person-name .first { color: var(--orange); }
  .person-title {
    font-size: 12px;
    color: var(--orange);
    margin-top: 2px;
  }
  .rule {
    position: absolute;
    left: 150px;
    right: 6px;
    top: 190px;
    height: 1px;
    background: var(--line);
  }

  .contacts {
    position: absolute;
    left: 28px;
    top: 237px;
    list-style: none;
    font-size: 12.5px;
    color: var(--text);
  }
  .contacts li {
    display: flex;
    align-items: center;
    gap: 9px;
    height: 16px;
  }
  .contacts svg { width: 9px; height: 9px; fill: var(--gray); }
  .contacts .accent { color: var(--orange); }

  .front-band {
    position: absolute;
    left: 0; bottom: 0;
    width: 555px; height: 14px;
  }

  /* back */
  .back-brand {
    position: absolute;
    left: 132px;
    top: 100px;
    display: flex;
    align-items: center;
    gap: 22px;
  }
  .back-brand .brand-dot {
    width: 58px; height: 58px;
    background: none;
    border: 6px solid var(--white);
  }
  .back-brand .brand-name {
    color: var(--white);
    font-size: 27px;
    line-height: 29px;
    letter-spacing: 5px;
  }
</style>
</head>
<body>
<main class="stage">
  <section class="card card-front" aria-label="Card front">
    <div class="front-brand">
      <span class="brand-dot"></span>
      <span class="brand-name">Velvet<br>Harbor</span>
    </div>

    <div class="person">
      <h1 class="person-name"><span class="first">Nessa</span> Pryle</h1>
      <p class="person-title">Founder &amp; Principal</p>
    </div>
    <div class="rule"></div>

    <ul class="contacts">
      <li>
        <svg viewBox="0 0 10 10"><path d="M2 0.5 L3.6 0.5 L4.3 2.8 L3.2 3.8 Q4.2 5.8 6.2 6.8 L7.2 5.7 L9.5 6.4 L9.5 8 Q9.5 9.5 8 9.5 Q1 9 0.5 2 Q0.5 0.5 2 0.5 Z"/></svg>
        <span>+1 628 309 4156</span>
      </li>
      <li>
        <svg viewBox="0 0 10 10"><path d="M0.5 2 H9.5 V8 H0.5 Z M1 2.3 L5 5.5 L9 2.3" stroke="#f4f4f4" stroke-width="0.8"/></svg>
        <span>nessa@velvetharbor.com</span>
      </li>
      <li>
        <svg viewBox="0 0 10 10"><circle cx="5" cy="5" r="4.5"/><path d="M0.5 5 H9.5 M5 0.5 Q2.5 5 5 9.5 M5 0.5 Q7.5 5 5 9.5" stroke="#f4f4f4" stroke-width="0.7" fill="none"/></svg>
        <span>www.<span class="accent">velvetharbor</span>.com</span>
      </li>
    </ul>

    <svg class="front-band" viewBox="0 0 555 14" preserveAspectRatio="none" aria-hidden="true">
      <rect x="0" y="0" width="555" height="14" fill="var(--gray)"/>
      <polygon points="0,0 402,0 394,14 0,14" fill="var(--orange)"/>
      <polygon points="408,0 414,0 406,14 400,14" fill="var(--card-white)"/>
      <polygon points="419,0 425,0 417,14 411,14" fill="var(--card-white)"/>
    </svg>
  </section>

  <section class="card card-back" aria-label="Card back">
    <div class="back-brand">
      <span class="brand-dot"></span>
      <span class="brand-name">Velvet<br>Harbor</span>
    </div>
  </section>
</main>
</body>
</html>
```